Web site for Tree Removal Company

What we are looking for:
-------------------------------
Looking for a wordpress web site, you can provide your own template or we can supply you with one (http://quorvel.plindatheme.net).

What we do
---------------
To see what we do please go to google Australia and google "Tree removal Sydney" or "Tree Removal Melbourne".

Web site requirements
-----------------------------
We prefer you to use our template as it has all our requirements in already.
- Responsive.
- Based on Wordpress.
- Full complaint and compatible with plugs.

Look, Feel and Appearance
------------------------------------
Please use the logo (see attached), for colour scheme, look and feel of the web site.

Thank you for your time and effort!

Target Market(s)

Tree Removal for Residential Homes

Industry/Entity Type

It Company

Number of Pages Required

4 page

Font styles to use
Serif
Sans Serif

Requirements
Must have
• Wordpress
Nice to have
• Original artwork, images and text
Should not have
• non related images or wording

```html
<!DOCTYPE html>
<html lang="en">
<head>
<meta charset="utf-8">
<title>Branchwell – Tree Cutting and Removal</title>
<link rel="stylesheet" href="https://fonts.googleapis.com/css2?family=Lato:wght@700;900&family=Open+Sans:ital,wght@0,300;0,400;1,300;1,400&display=swap">
<style>
  :root {
    --ink: #1a1a1a;
    --black: #000000;
    --footer: #262626;
    --orange: #f26522;
    --green: #6fd08c;
    --trunk: #a58c7c;
    --white: #ffffff;
    --hero-light: #f4efeb;
    --hero-mid: #d9cfc8;
  }
  * { box-sizing: border-box; margin: 0; padding: 0; }
  html, body { width: 857px; height: 1200px; overflow: hidden; background: var(--white); }
  body { position: relative; font-family: "Open Sans", Arial, sans-serif; color: var(--ink); }

  .site-header { position: absolute; left: 0; top: 0; width: 857px; height: 90px; background: var(--black); z-index: 2; }
  .nav-link { position: absolute; top: 35px; font-family: "Lato", Arial, sans-serif; font-weight: 900; font-size: 12px; color: var(--white); letter-spacing: 0.2px; white-space: nowrap; }
  .nav-link .caret { font-size: 9px; margin-left: 10px; }
  .btn-quote { display: block; background: var(--orange); color: var(--white); font-family: "Lato", Arial, sans-serif; font-weight: 900; font-size: 12px; text-align: center; border-radius: 17px; line-height: 32px; }
  .header-cta { position: absolute; left: 676px; top: 26px; width: 137px; }

  .brand { position: absolute; left: 368px; top: 6px; width: 120px; text-align: center; z-index: 3; }
  .brand-mark { display: block; width: 70px; height: 70px; margin: 0 auto; border-radius: 50%; background: var(--green); }
  .brand-name { display: block; margin-top: 22px; font-family: "Open Sans", Arial, sans-serif; font-weight: 400; font-size: 15px; letter-spacing: 2px; color: var(--ink); }

  .hero { position: absolute; left: 0; top: 90px; width: 857px; height: 324px; background: linear-gradient(135deg, var(--hero-mid) 0%, var(--hero-light) 40%, var(--hero-light) 65%, var(--hero-mid) 100%); }
  .call-line { position: absolute; right: 49px; top: 22px; text-align: right; font-size: 17px; line-height: 19px; color: var(--ink); }
  .call-line strong { color: var(--orange); font-weight: 700; }
  .call-icon { position: absolute; left: -36px; top: 2px; }
  .hero-title { position: absolute; left: 0; top: 110px; width: 857px; text-align: center; font-family: "Lato", Arial, sans-serif; font-weight: 900; font-size: 31px; line-height: 30px; color: var(--black); text-transform: uppercase; }
  .hero-lead { position: absolute; left: 0; top: 188px; width: 857px; text-align: center; font-weight: 300; font-size: 18.5px; line-height: 23px; color: var(--ink); }

  .services-title { position: absolute; left: 0; top: 435px; width: 857px; text-align: center; font-family: "Lato", Arial, sans-serif; font-weight: 900; font-size: 29px; color: var(--ink); }
  .service-tile { position: absolute; width: 218px; height: 183px; display: flex; align-items: center; justify-content: center; text-align: center; }
  .service-tile span { font-family: "Lato", Arial, sans-serif; font-weight: 900; font-size: 21px; line-height: 22px; color: var(--white); text-transform: uppercase; text-shadow: 0 1px 3px rgba(0,0,0,0.5); }
  .tile-removals { left: 58px; top: 497px; background: linear-gradient(160deg, #7d8a78, #4e4a3e); }
  .tile-stump { left: 290px; top: 497px; background: radial-gradient(circle at 50% 45%, #b08a68, #6e5238); }
  .tile-chipping { left: 522px; top: 497px; background: linear-gradient(150deg, #9cc04a, #3d5a2c 60%, #2b3440); }
  .tile-pruning { left: 58px; top: 694px; background: linear-gradient(170deg, #a5b0bd, #5c6347 55%, #3e4430); }
  .tile-palm { left: 290px; top: 694px; background: linear-gradient(160deg, #4b6b38, #2e4323); }
  .tile-reports { left: 522px; top: 694px; background: linear-gradient(140deg, #d7dadc, #a7adb1); }

  .reviews-title { position: absolute; left: 0; top: 915px; width: 857px; text-align: center; font-family: "Lato", Arial, sans-serif; font-weight: 900; font-size: 16px; color: var(--black); }
  .review { position: absolute; top: 978px; width: 245px; text-align: center; font-style: italic; font-weight: 400; font-size: 15.5px; line-height: 20px; color: var(--ink); }
  .review .mark { color: var(--green); font-weight: 700; font-style: normal; font-family: "Lato", Arial, sans-serif; }
  .review-1 { left: 12px; }
  .review-2 { left: 291px; }
  .review-3 { left: 563px; }
  .footer-cta { position: absolute; left: 364px; top: 1086px; width: 137px; }

  .site-footer { position: absolute; left: 0; top: 1153px; width: 857px; height: 47px; background: var(--footer); }
  .copyright { position: absolute; left: 42px; top: 15px; font-size: 10.5px; color: var(--white); }
  .social { position: absolute; right: 42px; top: 12px; display: flex; gap: 9px; }
  .social-dot { width: 22px; height: 22px; border-radius: 50%; background: var(--white); }
</style>
</head>
<body>
  <header class="site-header">
    <span class="nav-link" style="left:43px">SERVICES<span class="caret">▼</span></span>
    <span class="nav-link" style="left:174px">LOCATIONS<span class="caret">▼</span></span>
    <span class="nav-link" style="left:303px">ABOUT US</span>
    <span class="nav-link" style="left:559px">CONTACT</span>
    <a class="btn-quote header-cta">GET A FREE QUOTE</a>
  </header>

  <div class="brand">
    <span class="brand-mark"></span>
    <span class="brand-name">BRANCHWELL</span>
  </div>

  <section class="hero" role="img" aria-label="Faded photo of a chainsaw cutting through timber">
    <div class="call-line">
      <svg class="call-icon" width="16" height="24" viewBox="0 0 16 24">
        <rect x="1.5" y="1.5" width="13" height="21" rx="2" fill="none" stroke="#1a1a1a" stroke-width="2.5"/>
        <line x1="6" y1="19" x2="10" y2="19" stroke="#1a1a1a" stroke-width="2"/>
      </svg>
      Call <strong>+61 400 555 019</strong><br>for a free quote
    </div>
    <h1 class="hero-title">Australia’s finest tree cutting<br>and removal services</h1>
    <p class="hero-lead">Our team of professional arborists are trained to deal with<br>any tree problem and find the appropriate solution.</p>
  </section>

  <h2 class="services-title">Our services</h2>
  <div class="service-tile tile-removals" role="img" aria-label="Chainsaw resting on cut logs"><span>Tree<br>Removals</span></div>
  <div class="service-tile tile-stump" role="img" aria-label="Cut tree stump among wood chips"><span>Stump<br>Grinding</span></div>
  <div class="service-tile tile-chipping" role="img" aria-label="Worker feeding branches into a wood chipper"><span>Chipping<br>Services</span></div>
  <div class="service-tile tile-pruning" role="img" aria-label="Arborist pruning an olive tree"><span>Tree<br>Pruning</span></div>
  <div class="service-tile tile-palm" role="img" aria-label="Palm trees in dense greenery"><span>Palm<br>Cleaning</span></div>
  <div class="service-tile tile-reports" role="img" aria-label="Printed report with charts on a desk"><span>Arborist<br>Reports</span></div>

  <h3 class="reviews-title">WHAT PEOPLE SAY ABOUT US</h3>
  <p class="review review-1"><span class="mark">“</span>Lorem ipsum dolor sit amet, consectetuer adipiscing elit. Donec odio. Quisque volutpat mattis eros.<span class="mark">”</span></p>
  <p class="review review-2"><span class="mark">“</span>Donec nec justo eget felis facilisis fermentum. Aliquam porttitor mauris sit amet orci.<span class="mark">”</span></p>
  <p class="review review-3"><span class="mark">“</span>Morbi in sem quis dui placerat ornare. Pellentesque odio nisi, euismod in, pharetra a, ultricies.<span class="mark">”</span></p>
  <a class="btn-quote footer-cta">GET A FREE QUOTE</a>

  <footer class="site-footer">
    <p class="copyright">Copyright © 2015 Branchwell</p>
    <div class="social">
      <span class="social-dot" aria-label="Social link"></span>
      <span class="social-dot" aria-label="Social link"></span>
      <span class="social-dot" aria-label="Social link"></span>
    </div>
  </footer>
</body>
</html>
```